HARBOUR LANE DECOR

We need a web design for a new business based in Bonny Hills (NSW). We are a small retail outlet on the Mid North Coast (NSW, Australia) selling home wares, gifts, beach wear, artwork, and hampers etc. We would like to a few different samples if that's not too much trouble (e.g. black and white vs colour, e.g. "beach colours").
We would like the website to communicate that we are an affordable, local (community based) business, with customer satisfaction at the forefront of our mind. We have a strong customer service focus, and in addition to retail sales we are now looking to expand into the online hamper business.
We are open 7 days (except public holidays).
Note: We like the design / layout of the "Cork Pail 'N' Shelf Website" if you would like to compare www.corkpailnshelf.com.au

Industry/Entity Type

Business

```html
<!DOCTYPE html>
<html lang="en">
<head>
<meta charset="utf-8">
<title>Harbour Lane Decor</title>
<link rel="stylesheet" href="https://fonts.googleapis.com/css2?family=Montserrat:wght@600;700&family=Raleway:wght@300;400;500;600&family=Playfair+Display:ital,wght@1,700&display=swap">
<style>
:root{
  --ink:#222222;
  --bar:#1f1f1f;
  --cyan:#12b5e6;
  --orange:#f7941d;
  --linen:#e6e1d6;
  --white:#ffffff;
  --text:#333333;
  --overlay:rgba(20,20,20,.78);
}
*{margin:0;padding:0;box-sizing:border-box}
html,body{width:1163px;height:1200px;overflow:hidden}
body{position:relative;background:var(--linen);font-family:"Raleway",sans-serif;color:var(--text)}
.topbar{position:absolute;left:0;top:0;width:1163px;height:42px;background:var(--bar);color:#eee;font-size:11.5px}
.topbar .ship{position:absolute;left:177px;top:14px;display:flex;align-items:center;gap:8px}
.topbar .links{position:absolute;left:606px;top:14px;display:flex;align-items:center;font-size:11px}
.topbar .links span{padding:0 9px;border-left:1px solid #aaa;line-height:12px}
.topbar .links span:first-child{border-left:none;padding-left:0}
.signin{position:absolute;left:852px;top:10px;width:63px;height:23px;background:var(--orange);color:#fff;font-size:11.5px;text-align:center;line-height:23px}
.register{position:absolute;left:921px;top:15px;font-size:11.5px}
.header{position:absolute;left:0;top:42px;width:1163px;height:72px;background:var(--white)}
.brand{position:absolute;left:177px;top:20px;display:flex;align-items:center;gap:8px;font-family:"Montserrat",sans-serif;font-weight:700;font-size:20px;color:var(--cyan);letter-spacing:.5px}
.brand i{width:14px;height:14px;background:var(--cyan);display:block}
.nav{position:absolute;left:491px;top:30px;display:flex;gap:30px;font-family:"Montserrat",sans-serif;font-weight:600;font-size:11px;color:var(--ink)}
.nav .on{color:var(--cyan)}
.card{position:absolute;left:179px;top:147px;width:806px;height:937px;background:var(--white);box-shadow:0 6px 22px rgba(0,0,0,.35)}
.hero-photo{position:absolute;left:12px;top:21px;width:502px;height:452px;background:linear-gradient(135deg,#8a7a5c,#d8cfb8 45%,#b89a6a 75%,#6d5a3e)}
.hero-panel{position:absolute;left:514px;top:21px;width:279px;height:400px;background:#161616;color:#fff;font-family:"Montserrat",sans-serif;font-weight:700;text-align:center}
.dots{position:absolute;right:10px;top:20px;display:flex;gap:7px}
.dots b{width:13px;height:13px;border:2px solid #fff;border-radius:50%;display:block}
.dots b.on{border-color:var(--cyan)}
.hero-panel .l1{position:absolute;left:0;width:100%;top:86px;font-size:42px;line-height:1}
.hero-panel .l2{position:absolute;left:0;width:100%;top:128px;font-size:62px;line-height:1;color:var(--cyan)}
.hero-panel .l3{position:absolute;left:0;width:100%;top:195px;font-size:60px;line-height:1}
.hero-panel .l4{position:absolute;left:0;width:100%;top:262px;font-size:24px;line-height:1;color:var(--cyan)}
.hero-panel .l5{position:absolute;left:0;width:100%;top:290px;font-size:64px;line-height:1.1}
.shop-now{position:absolute;left:514px;top:421px;width:279px;height:52px;background:var(--cyan);color:#fff;font-family:"Montserrat",sans-serif;font-weight:600;font-size:19px;text-align:center;line-height:52px}
.tagline{position:absolute;left:0;top:506px;width:806px;text-align:center;font-weight:300;font-size:25px;color:#444}
.tile{position:absolute;top:559px;width:244px;height:167px;overflow:hidden}
.tile .band,.promo .band{position:absolute;background:var(--overlay);color:#fff;text-align:center}
.tile .band{left:0;top:59px;width:100%;height:66px}
.title{font-weight:300;font-size:26px;letter-spacing:.5px;display:block}
.shoplink{font-family:"Playfair Display",serif;font-style:italic;font-weight:700;font-size:13px;display:block}
.tile .title{padding-top:8px}
.promo{position:absolute;top:746px;width:390px;height:184px}
.promo .band{left:33px;top:59px;width:176px;height:61px;text-align:left;padding-left:16px;background:rgba(60,50,40,.7)}
.promo .title{padding-top:6px}
.footer{position:absolute;left:0;top:1115px;width:1163px;height:85px;background:var(--bar);color:#fff}
.row{position:absolute;left:174px;top:12px;display:flex;align-items:center;height:22px;font-family:"Montserrat",sans-serif;font-weight:600;font-size:11.5px}
.label{color:var(--cyan)}
.icons{display:flex;gap:8px;margin:0 28px 0 16px}
.icons i{width:13px;height:13px;background:#ddd;border-radius:2px;display:block}
.cards{display:flex;gap:3px;margin:0 32px 0 12px}
.cards i{width:20px;height:12px;background:#ccc;border-radius:1px;display:block}
.email{margin-left:7px;width:206px;height:21px;background:#444;color:#ddd;font-family:"Raleway",sans-serif;font-weight:500;font-size:10px;line-height:21px;padding-left:5px}
.subscribe{width:62px;height:21px;background:var(--cyan);color:#fff;font-family:"Raleway",sans-serif;font-weight:500;font-size:10px;line-height:21px;text-align:center}
.copy{position:absolute;left:0;top:48px;width:1163px;text-align:center;font-size:13.5px}
</style>
</head>
<body>
<div class="topbar">
  <div class="ship"><svg width="15" height="11" viewBox="0 0 15 11"><rect x="0" y="1" width="9" height="7" fill="#12b5e6"/><path d="M9 3h3l3 3v2H9z" fill="#12b5e6"/><circle cx="3" cy="9" r="1.8" fill="#12b5e6"/><circle cx="12" cy="9" r="1.8" fill="#12b5e6"/></svg>Free Shipping On Orders Over $200</div>
  <div class="links"><span>Shopping Cart</span><span>Checkout</span><span>Track Order</span></div>
  <div class="signin">SIGN IN</div>
  <div class="register">REGISTER</div>
</div>
<header class="header">
  <div class="brand"><i></i>Harbour Lane Decor</div>
  <nav class="nav"><span class="on">HOME</span><span>ABOUT US</span><span>PRODUCTS</span><span>FAQ'S</span><span>TESTIMOINIALS</span><span>CONTACT US</span></nav>
</header>
<main class="card">
  <div class="hero-photo" role="img" aria-label="Photo of the shop interior with shelves of cushions, towels and home wares"></div>
  <div class="hero-panel">
    <div class="dots"><b class="on"></b><b></b><b></b><b></b></div>
    <div class="l1">HARBOUR</div>
    <div class="l2">LANE</div>
    <div class="l3">DECOR</div>
    <div class="l4">SANDY COVE NSW</div>
    <div class="l5">OFFER</div>
  </div>
  <div class="shop-now">SHOP NOW</div>
  <h2 class="tagline">FRESH IDEAS &amp; INSPIRATION FOR YOUR HOME AND LIFESTYLE</h2>
  <div class="tile" style="left:12px;background:linear-gradient(160deg,#c9b89a,#8c6d4b 60%,#d9d2c4)" role="img" aria-label="Photo of home wares on display">
    <div class="band"><span class="title">HOME WARES</span><span class="shoplink">Shop Now &gt;</span></div></div>
  <div class="tile" style="left:281px;background:linear-gradient(160deg,#8fa0a8,#a77a55 55%,#3f6b5d)" role="img" aria-label="Photo of artwork and ceramics">
    <div class="band"><span class="title">ARTWORK</span><span class="shoplink">Shop Now &gt;</span></div></div>
  <div class="tile" style="left:550px;background:linear-gradient(160deg,#3d6b7a,#c8c0b0 50%,#b9463e)" role="img" aria-label="Photo of beach wear and cushions on shelves">
    <div class="band"><span class="title">BEACH WEAR</span><span class="shoplink">Shop Now &gt;</span></div></div>
  <div class="promo" style="left:12px;background:linear-gradient(120deg,#d9c29a,#8a5a2c 55%,#2e3a2c)" role="img" aria-label="Photo of a gift wrapped with a ribbon">
    <div class="band"><span class="title">GIFTS</span><span class="shoplink">Shop Now &gt;</span></div></div>
  <div class="promo" style="left:402px;width:391px;background:linear-gradient(180deg,#e4e4e6,#c8c4c0 55%,#8a5e38)" role="img" aria-label="Photo of a wrapped hamper basket with a bow">
    <div class="band" style="background:rgba(60,60,60,.75)"><span class="title">HAMPERS</span><span class="shoplink">Shop Now &gt;</span></div></div>
</main>
<footer class="footer">
  <div class="row">
    <span class="label">FOLLOW US</span>
    <span class="icons"><i></i><i></i><i></i><i></i><i></i></span>
    <span class="label">PAYMENT</span>
    <span class="cards"><i></i><i></i><i></i><i></i><i></i></span>
    <span class="label">SIGN UP NEWSLETTER</span>
    <span class="email">E-mail Newsletter</span><span class="subscribe">SUBSCRIBE</span>
  </div>
  <div class="copy">© Company Name ® Pty Ltd 2014 | Privacy | Terms &amp; Conditions | Sitemap</div>
</footer>
</body>
</html>
```